Bref créative
Business Cards/Stationary for a Consulting Company
Darvey Solutions
Simple
Lorette Darvey
PO BOX 4087
Larkmoor, ST 00000
lorette@darveysolutions-example.com
www.darveysolutions-example.com

```html
<!DOCTYPE html>
<html lang="en">
<head>
<meta charset="utf-8">
<title>Darvey Solutions Stationery Set</title>
<link href="https://fonts.googleapis.com/css2?family=Montserrat:wght@400;600;700&display=swap" rel="stylesheet">
<style>
:root{
  --bg:#8e8e90;
  --bg-dark:#6f6f72;
  --paper:#ffffff;
  --brand:#1b3f9a;
  --brand-deep:#0a2470;
  --brand-light:#2f7fd6;
  --ink:#3a3f4a;
  --label:#e9e9ea;
  --fold:#c9ccd4;
}
*{margin:0;padding:0;box-sizing:border-box}
html,body{width:1200px;height:554px;overflow:hidden}
body{font-family:"Montserrat",Arial,sans-serif;background:linear-gradient(180deg,var(--bg) 0%,var(--bg-dark) 100%);position:relative;color:var(--ink)}
.item{position:absolute;background:var(--paper);box-shadow:2px 3px 6px rgba(0,0,0,.35)}
.label{position:absolute;top:-10px;left:0;width:100%;text-align:center;font-size:5px;color:var(--label);letter-spacing:.2px;white-space:nowrap}
.logo{display:flex;align-items:center;gap:3px;position:absolute;color:var(--brand);font-weight:700;white-space:nowrap}
.logo .dot{border-radius:50%;background:var(--brand);flex:none}
.logo.sm{font-size:5px}.logo.sm .dot{width:8px;height:8px}
.logo.md{font-size:7px}.logo.md .dot{width:11px;height:11px}
.logo.rev{color:#fff}.logo.rev .dot{background:#fff}
.centered{left:50%;transform:translateX(-50%)}
.note .logo{top:10px}
.card .logo{top:12px}
.card.blue{background:linear-gradient(135deg,var(--brand-light) 0%,var(--brand) 55%,var(--brand-deep) 100%)}
.contact{position:absolute;font-size:3px;line-height:4.5px;color:var(--ink);white-space:nowrap}
.letter .logo{top:12px}
.letter .footer{position:absolute;bottom:8px;left:0;width:100%;text-align:center;font-size:3px;color:var(--ink);white-space:nowrap}
.band{position:absolute;left:0;bottom:0;width:100%;height:4px;background:linear-gradient(90deg,var(--brand-deep),var(--brand-light))}
.env .logo{top:8px;left:8px}
.env .contact{top:22px;left:8px}
.env-back{background:none}
.env-back svg{display:block}
</style>
</head>
<body>

<div class="item note" style="left:110px;top:19px;width:92px;height:87px"><span class="label">Notepad Design 1</span><div class="logo sm centered"><span class="dot"></span>DARVEY SOLUTIONS</div></div>
<div class="item note" style="left:216px;top:19px;width:92px;height:87px"><span class="label">Notepad Design 2</span><div class="logo sm centered"><span class="dot"></span>DARVEY SOLUTIONS</div></div>
<div class="item note" style="left:110px;top:120px;width:92px;height:91px"><span class="label">Notepad Design 3</span><div class="logo sm centered"><span class="dot"></span>DARVEY SOLUTIONS</div></div>
<div class="item note" style="left:216px;top:120px;width:92px;height:91px"><span class="label">Notepad Design 4</span><div class="logo sm centered"><span class="dot"></span>DARVEY SOLUTIONS</div></div>

<div class="item card" style="left:324px;top:163px;width:84px;height:55px"><span class="label">Business Card Front 1</span><div class="logo sm centered"><span class="dot"></span>DARVEY SOLUTIONS</div></div>
<div class="item card" style="left:425px;top:163px;width:86px;height:55px"><span class="label">Business Card Back 1</span>
  <div class="contact" style="top:8px;left:6px"><b>Lorette Darvey</b><br>PO BOX 4087<br>Larkmoor, ST 00000<br>lorette@darveysolutions-example.com<br>www.darveysolutions-example.com</div></div>
<div class="item card" style="left:528px;top:163px;width:86px;height:55px"><span class="label">Business Card Front 2</span>
  <div class="logo sm" style="top:6px;left:6px"><span class="dot"></span>DARVEY SOLUTIONS</div>
  <div class="contact" style="top:22px;left:6px"><b>Lorette Darvey</b><br>PO BOX 4087, Larkmoor, ST 00000<br>www.darveysolutions-example.com</div><div class="band" style="height:3px"></div></div>
<div class="item card blue" style="left:629px;top:158px;width:91px;height:60px"><span class="label">Business Card Back 2</span><div class="logo sm rev centered" style="top:24px"><span class="dot"></span>DARVEY SOLUTIONS</div></div>
<div class="item card" style="left:732px;top:163px;width:89px;height:55px"><span class="label">Business Card Front 3</span><div class="logo sm centered" style="top:16px"><span class="dot"></span>DARVEY SOLUTIONS</div>
  <div class="contact" style="top:32px;left:0;width:100%;text-align:center">Lorette Darvey · PO BOX 4087</div></div>
<div class="item card blue" style="left:828px;top:158px;width:89px;height:60px"><span class="label">Business Card Back 3</span><div class="logo sm rev centered" style="top:24px"><span class="dot"></span>DARVEY SOLUTIONS</div></div>

<div class="item env" style="left:936px;top:106px;width:187px;height:106px"><span class="label">Envelope Front</span>
  <div class="logo sm"><span class="dot"></span>DARVEY SOLUTIONS</div>
  <div class="contact">PO BOX 4087<br>Larkmoor, ST 00000</div></div>
<div class="item env" style="left:936px;top:233px;width:187px;height:106px"><span class="label">Envelope Front</span>
  <div class="logo sm"><span class="dot"></span>DARVEY SOLUTIONS</div>
  <div class="contact">PO BOX 4087<br>Larkmoor, ST 00000</div><div class="band" style="height:3px"></div></div>

<div class="item env-back" style="left:946px;top:355px;width:177px;height:80px;box-shadow:none"><span class="label">Envelope Back</span>
  <svg width="177" height="80" viewBox="0 0 177 80">
    <rect width="177" height="80" fill="#fff"/>
    <path d="M0 0 L88.5 44 L177 0" fill="none" stroke="var(--fold)" stroke-width="1"/>
  </svg></div>
<div class="item env-back" style="left:946px;top:418px;width:177px;height:115px">
  <svg width="177" height="115" viewBox="0 0 177 115">
    <defs><linearGradient id="flap" x1="0" y1="0" x2="1" y2="1"><stop offset="0" stop-color="#2f7fd6"/><stop offset="1" stop-color="#0a2470"/></linearGradient></defs>
    <rect width="177" height="115" fill="#fff"/>
    <path d="M0 0 H177 L88.5 52 Z" fill="url(#flap)"/>
  </svg></div>

<div class="item letter" style="left:24px;top:233px;width:211px;height:305px"><span class="label">Letterhead Page 1</span>
  <div class="logo md centered"><span class="dot"></span>DARVEY SOLUTIONS</div>
  <div class="footer">PO BOX 4087 · Larkmoor, ST 00000 · lorette@darveysolutions-example.com · www.darveysolutions-example.com</div></div>
<div class="item letter" style="left:254px;top:233px;width:202px;height:305px"><span class="label">Letterhead Page 2</span>
  <div class="logo md" style="left:10px"><span class="dot"></span>DARVEY SOLUTIONS</div>
  <div class="contact" style="top:12px;right:10px;text-align:right">PO BOX 4087<br>Larkmoor, ST 00000<br>www.darveysolutions-example.com</div></div>
<div class="item letter" style="left:475px;top:233px;width:216px;height:305px"><span class="label">Letterhead Page 3</span>
  <div class="logo md centered"><span class="dot"></span>DARVEY SOLUTIONS</div>
  <div class="footer">PO BOX 4087 · Larkmoor, ST 00000 · www.darveysolutions-example.com</div><div class="band"></div></div>
<div class="item letter" style="left:706px;top:233px;width:206px;height:305px"><span class="label">Letterhead Page 4</span>
  <div class="logo md" style="left:10px"><span class="dot"></span>DARVEY SOLUTIONS</div>
  <div class="contact" style="top:12px;right:10px;text-align:right">PO BOX 4087<br>Larkmoor, ST 00000<br>www.darveysolutions-example.com</div><div class="band"></div></div>

</body>
</html>
```